K7 clearline

We are a glazing company specializing in frameless glass .
I would like the business cards in black with the logo taking up the most part of the front added with " frameless glass specialist's " below it.
On the back side I would like a list of what we do :
• shower screens
• glass balustrade / pool fencing
• mirrors
•office partitions
• sky lights
•shop fronts
•splash backs
Also include this information :
📧 - marcus@k7clearline.com
📞Marcus - 0412967528
📞 Colin - 0457 213 684
Updates
To all designs already posted can you include on the back of the card in the services part -
•splash backs
Target Market(s)
High end builders
Industry/Entity Type
Glazing
Contact Information for Business Card
On the back side I would like a list of what we do : • shower screens • glass balustrade / pool fencing • mirrors •office partitions • sky lights •shop fronts Also include this information : 📧 - marcus@k7clearline.com 📞Marcus - 0412967528 📞 Colin - 0457 213 684
Colors
Designer to choose colors to be used in the design.
Look and feel
Each slider illustrates characteristics of the customer's brand and the style your logo design should communicate.

```html
<!DOCTYPE html>
<html lang="en">
<head>
<meta charset="utf-8">
<title>K7 clearline business cards</title>
<link rel="stylesheet" href="https://fonts.googleapis.com/css2?family=Montserrat:wght@500;600;700&family=Oswald:wght@500&display=swap">
<style>
  :root {
    --page: #5a5a5a;
    --card: #050505;
    --white: #ffffff;
    --teal: #4cc9a8;
    --teal-deep: #2aa3a8;
    --blue: #1b6a8c;
    --ink: #0a1a1c;
  }
  * { box-sizing: border-box; margin: 0; padding: 0; }
  html, body { width: 1200px; height: 1200px; overflow: hidden; }
  body {
    background: var(--page);
    font-family: "Montserrat", sans-serif;
    position: relative;
  }
  .card {
    position: absolute;
    left: 100px;
    width: 1000px;
    height: 540px;
    background: var(--card);
    border-radius: 40px;
    overflow: hidden;
    border-bottom: 4px solid var(--teal-deep);
  }
  .card--back { top: 45px; }
  .card--front { top: 615px; }

  /* back side */
  .accent-band { position: absolute; inset: 0; width: 100%; height: 100%; }
  .services {
    position: absolute;
    left: 70px;
    top: 120px;
  }
  .services__title {
    font-weight: 700;
    font-size: 40px;
    letter-spacing: 2px;
    color: var(--teal);
    margin-bottom: 14px;
  }
  .services__list { list-style: none; }
  .services__item {
    font-family: "Oswald", sans-serif;
    font-weight: 500;
    font-size: 27px;
    line-height: 38px;
    color: var(--white);
    text-transform: uppercase;
    display: flex;
    align-items: center;
    gap: 18px;
    padding-left: 30px;
  }
  .services__item::before {
    content: "";
    width: 13px;
    height: 13px;
    background: var(--teal);
    transform: rotate(45deg);
    flex: none;
  }
  .brand-block {
    position: absolute;
    left: 560px;
    top: 80px;
    width: 410px;
  }
  .brand-name {
    font-weight: 700;
    font-size: 44px;
    line-height: 1;
    color: var(--white);
    text-transform: uppercase;
    letter-spacing: 1px;
    white-space: nowrap;
    margin-bottom: 40px;
  }
  .contact {
    display: grid;
    grid-template-columns: 34px auto;
    column-gap: 12px;
    align-items: end;
    margin-bottom: 14px;
    padding-left: 60px;
  }
  .contact__icon { width: 30px; height: 30px; margin-bottom: 6px; }
  .contact__name {
    grid-column: 2;
    font-weight: 500;
    font-size: 26px;
    color: var(--teal);
    line-height: 1;
  }
  .contact__phone {
    grid-column: 2;
    font-weight: 600;
    font-size: 34px;
    color: var(--white);
    line-height: 1.1;
    white-space: nowrap;
  }
  .contact .contact__icon { grid-row: 2; grid-column: 1; }
  .email {
    position: absolute;
    right: 50px;
    bottom: 34px;
    display: flex;
    align-items: center;
    gap: 12px;
    font-weight: 500;
    font-size: 24px;
    line-height: 1;
    color: var(--ink);
    white-space: nowrap;
  }
  .email__icon { width: 30px; height: 22px; flex: none; }

  /* front side */
  .front-brand {
    position: absolute;
    inset: 0;
    display: flex;
    flex-direction: column;
    align-items: center;
    justify-content: center;
    gap: 40px;
  }
  .front-brand__name {
    font-weight: 700;
    font-size: 110px;
    line-height: 1;
    color: var(--white);
    text-transform: uppercase;
    letter-spacing: 2px;
  }
  .front-brand__tagline {
    font-weight: 700;
    font-size: 38px;
    letter-spacing: 3px;
    color: var(--teal);
    text-transform: uppercase;
  }
</style>
</head>
<body>

<section class="card card--back" aria-label="Business card back">
  <svg class="accent-band" viewBox="0 0 1000 540" preserveAspectRatio="none" aria-hidden="true">
    <defs>
      <linearGradient id="band-gradient" x1="0" y1="1" x2="1" y2="0">
        <stop offset="0" stop-color="#1b6a8c"/>
        <stop offset="0.55" stop-color="#2aa3a8"/>
        <stop offset="1" stop-color="#4cc9a8"/>
      </linearGradient>
    </defs>
    <path d="M0 522 L470 522 C540 522 540 430 610 430 L1000 430 L1000 540 L0 540 Z" fill="url(#band-gradient)"/>
  </svg>

  <div class="services">
    <h2 class="services__title">SERVICES</h2>
    <ul class="services__list">
      <li class="services__item">Shower screens</li>
      <li class="services__item">Glass balustrade / pool fencing</li>
      <li class="services__item">Mirrors</li>
      <li class="services__item">Office partitions</li>
      <li class="services__item">Sky lights</li>
      <li class="services__item">Shop fronts</li>
      <li class="services__item">Splash backs</li>
    </ul>
  </div>

  <div class="brand-block">
    <p class="brand-name">K7 clearline</p>
    <div class="contact">
      <span class="contact__name">Marcus</span>
      <svg class="contact__icon" viewBox="0 0 24 24" aria-hidden="true"><path fill="#4cc9a8" d="M6.6 10.8a15.2 15.2 0 0 0 6.6 6.6l2.2-2.2a1 1 0 0 1 1-.25 11.4 11.4 0 0 0 3.6.57 1 1 0 0 1 1 1V20a1 1 0 0 1-1 1A17 17 0 0 1 3 4a1 1 0 0 1 1-1h3.5a1 1 0 0 1 1 1c0 1.25.2 2.45.57 3.6a1 1 0 0 1-.25 1z"/></svg>
      <span class="contact__phone">0412 967 528</span>
    </div>
    <div class="contact">
      <span class="contact__name">Colin</span>
      <svg class="contact__icon" viewBox="0 0 24 24" aria-hidden="true"><path fill="#4cc9a8" d="M6.6 10.8a15.2 15.2 0 0 0 6.6 6.6l2.2-2.2a1 1 0 0 1 1-.25 11.4 11.4 0 0 0 3.6.57 1 1 0 0 1 1 1V20a1 1 0 0 1-1 1A17 17 0 0 1 3 4a1 1 0 0 1 1-1h3.5a1 1 0 0 1 1 1c0 1.25.2 2.45.57 3.6a1 1 0 0 1-.25 1z"/></svg>
      <span class="contact__phone">0457 213 684</span>
    </div>
  </div>

  <p class="email">
    <svg class="email__icon" viewBox="0 0 30 22" aria-hidden="true"><rect x="1" y="1" width="28" height="20" fill="#0a1a1c"/><path d="M2 2 L15 13 L28 2" fill="none" stroke="#4cc9a8" stroke-width="2"/></svg>
    <span class="email__address">marcus@k7clearline.com</span>
  </p>
</section>

<section class="card card--front" aria-label="Business card front">
  <div class="front-brand">
    <p class="front-brand__name">K7 clearline</p>
    <p class="front-brand__tagline">Frameless glass specialist's</p>
  </div>
</section>

</body>
</html>
```